Modern Business Card for Larkwell 2018

Our company assumes the best about people. We are creating an online community of entrepreneurs and business leaders who struggle with marketing their business online.

This business card should POP! We recently got a new logo and are launching a new website next month, so our business cards should make a statement that feels:
-Fresh
-Smart
-Trustworthy
-Fun

Target Market(s)

small business owners, entrepreneurs

Industry/Entity Type

Digital Marketing

Contact Information for Business Card

Dimensions: 3.5" x 2"

Font styles to use
Sans Serif

Colors
f37122
ffffff

Requirements
Must have
• We need a business card with a modern, bold design. We will use one side of the card as a lead-generation offer, so text on one side will need to fit up to 140 characters. The business card should stick to our core colors (orange, black, and white).
Nice to have
• We think a vertical "portrait" design could be interesting.
Should not have
• Should not look like a traditional business card. The round icon should stand out from a distance.

```html
<!DOCTYPE html>
<html lang="en">
<head>
<meta charset="utf-8">
<title>Larkwell Business Card</title>
<link rel="stylesheet" href="https://fonts.googleapis.com/css2?family=Open+Sans:wght@400;600;700&family=Montserrat:wght@700&family=Yellowtail&family=Kalam:wght@700&display=swap">
<style>
  :root {
    --orange: #f37122;
    --card-orange: #e8622a;
    --white: #ffffff;
    --paper: #f3f3f3;
    --ink: #1f1f1f;
    --ink-soft: #4a4a4a;
    --backdrop: #2b2b2b;
    --rule: rgba(255,255,255,0.55);
  }
  * { box-sizing: border-box; margin: 0; padding: 0; }
  html, body { width: 1200px; height: 960px; overflow: hidden; }
  body {
    background: var(--backdrop);
    position: relative;
    font-family: "Open Sans", Arial, sans-serif;
  }
  .card {
    position: absolute;
    width: 600px;
    height: 342px;
    overflow: hidden;
    box-shadow: 0 4px 10px rgba(0,0,0,0.5);
  }

  /* Front */
  .card-front { left: 321px; top: 108px; background: var(--card-orange); }
  .front-panel {
    position: absolute; inset: 0;
    background: var(--paper);
    border-radius: 128px 0 126px 0 / 157px 0 160px 0;
  }
  .brand-disc {
    position: absolute;
    left: 409px; top: 22px;
    width: 186px; height: 186px;
    border-radius: 50%;
    background: var(--card-orange);
    display: flex; align-items: center; justify-content: center;
    color: var(--white);
    font-family: "Montserrat", Arial, sans-serif;
    font-weight: 700;
    font-size: 28px;
    letter-spacing: 0.5px;
  }
  .person-name {
    position: absolute; left: 30px; top: 214px;
    font-family: "Yellowtail", cursive;
    font-size: 46px;
    color: var(--card-orange);
    transform: rotate(-3deg);
    transform-origin: left bottom;
  }
  .person-role {
    position: absolute; left: 32px; top: 276px;
    font-weight: 700; font-size: 15.5px; color: var(--ink);
  }
  .person-email {
    position: absolute; left: 32px; top: 294px;
    font-size: 15px; color: var(--ink-soft);
  }

  /* Back */
  .card-back { left: 320px; top: 493px; background: var(--card-orange); color: var(--white); }
  .brand-block {
    position: absolute; left: 44px; top: 58px; width: 240px;
    text-align: center;
  }
  .brand-dot {
    width: 38px; height: 38px; border-radius: 50%;
    background: var(--white); margin: 0 auto 8px;
  }
  .brand-name {
    font-family: "Montserrat", Arial, sans-serif;
    font-weight: 700; font-size: 34px; line-height: 1; letter-spacing: 0.5px;
  }
  .brand-tagline {
    font-family: "Kalam", cursive; font-weight: 700;
    font-size: 11px; letter-spacing: 0.6px; margin-top: 6px;
    text-transform: uppercase;
  }
  .divider {
    position: absolute; left: 297px; top: 28px;
    width: 1px; height: 162px; background: var(--rule);
  }
  .offer { position: absolute; left: 323px; top: 26px; }
  .offer-headline {
    font-family: "Open Sans", Arial, sans-serif;
    font-weight: 700; font-size: 19.5px; line-height: 22px;
    text-transform: uppercase;
  }
  .offer-body { font-size: 14.5px; line-height: 20px; margin-top: 6px; }
  .offer-link { font-weight: 700; font-size: 17px; margin-top: 9px; }
  .note-box {
    position: absolute; left: 20px; top: 217px;
    width: 557px; height: 101px;
    background: var(--paper); border-radius: 16px;
  }
  .note-line {
    position: absolute; left: 24px; right: 27px;
    height: 1px; background: #333;
  }
  .note-line.first { top: 31px; }
  .note-line.second { top: 71px; }
</style>
</head>
<body>
  <section class="card card-front">
    <div class="front-panel"></div>
    <div class="brand-disc">Larkwell</div>
    <div class="person-name">Dana Whitfield</div>
    <div class="person-role">Story Marketing Coach</div>
    <div class="person-email">dana@larkwellnow.com</div>
  </section>

  <section class="card card-back">
    <div class="brand-block">
      <div class="brand-dot"></div>
      <div class="brand-name">LARKWELL</div>
      <div class="brand-tagline">Tell stories that inspire action</div>
    </div>
    <div class="divider"></div>
    <div class="offer">
      <p class="offer-headline">Reach more people.<br>Make more money.<br>Create more impact.</p>
      <p class="offer-body">Get your free Larkwell<br>Starter Package and our<br>marketing guide today at</p>
      <p class="offer-link">Larkwellnow.com/start</p>
    </div>
    <div class="note-box">
      <div class="note-line first"></div>
      <div class="note-line second"></div>
    </div>
  </section>
</body>
</html>
```